Velmor Crest - Advanced Skincare and undetectable Makeup for Men

We are in need of a professional webpage for our company Velmor Crest. We help every man feel his best by looking his best. Inspired by the myth of Adonis, we offer makeup and skincare products along with education upon their use. Our mission is to celebrate masculinity in all of its forms, regardless of age, race, sexual orientation, or assigned gender at birth.

The webpage would serve as our online store, as a place where our clients can learn about our brand, view our "How-to" video tutorials, and get product information. An online blog will also be hosted in order to keep clients up to date with news, updates, media mentions, etc.

The color schemes that we use are mostly Black and Gold, with Red accents. please keep in mind that this is a men's cosmetics line, and therefore should read powerful, sexy, confident and bold - all with a high end look and feel.

Think along the lines of brands like Dirk Halvan, QBN, Belcuzzi, etc.

our logo is included in the files attached. images and copy will be added in at a later time; hence, general images that fit the feel and filler text is encouraged.

The products to be sold include:
a face cleanser in a pump dispenser bottle (1 size)
a mask in a round jar container (1 size)
a moisturizer in a pump container 1 size)
a concealer in a click pen with a brush applicator (3 shades)
a liquid liner pen (4 shades)
a contouring palette (2 shade options)
a setting spray (single option)

Target Market(s)

Millennial Men

Industry/Entity Type

Beauty

Number of Pages Required

5+ page

Font styles to use
Serif

Colors
ec1f27
000000
faa54b

Requirements
Must have
• ur essential requirements are:
• 1) a stunning and engaging landing page that truly captures the ideals of sexuality, boldness and confidence.
• 2) an interactive and engaging online store that is easy to update / add product / information to.
• 3) Product pages supporting various toggling images of the product, a shade selection option, ingredient information, usage instructions, pricing, and a link to a "how to video" unique to each individual product.
• 4) dedicated space where all of the tutorials can be organized together
• 5) an organized Blog section, that would include a segment for a Q&A section for us to update as the brand grows, ongoing contests (that would be easily hidden if there are no contests running at the moment) as well as general news and updates segment.
• 6) an "about us" page, where our customers are able to learn about our story, inspirations, humanitarian efforts and philosophies in product contents and purity.
• 7) a contact us page, which would include social media links, contact email and telephone number as well as physical address to be updated upon launch.
• 8) discrete privacy policy, terms of use, and return policy links available at the bottom of every page
Nice to have
• 1) A posting forum where clients could post their looks using our products, or maybe a live stream of our Pictoloop account.
• 2) a member sign in page so that we can collect and store customer information for faster check out, keep track of purchases attached to their email address (future loyalty program plans) and maintain an email database for email notifications and the such.

```html
<!DOCTYPE html>
<html lang="en">
<head>
<meta charset="utf-8">
<title>Velmor Crest — Skincare and Makeup for Men</title>
<link href="https://fonts.googleapis.com/css2?family=Cinzel:wght@500&family=Montserrat:wght@400;500;600;700&display=swap" rel="stylesheet">
<style>
:root{
  --black:#000;
  --ink:#111;
  --gold:#b8823a;
  --gold-dark:#8e6426;
  --red:#ec1f27;
  --page:#d8d8d6;
  --band:#c4c4c2;
  --card:#fff;
  --tile:#ececea;
  --muted:#8a8a8a;
  --btn:#b1b1af;
  --footer-text:#8c8c8c;
}
*{box-sizing:border-box;margin:0;padding:0}
html,body{width:1200px;height:2455px;overflow:hidden}
body{position:relative;background:var(--page);font-family:'Montserrat',sans-serif;color:var(--ink)}
.abs{position:absolute}

/* header */
.hero{left:0;top:0;width:1200px;height:548px;background:#0b0b0b;overflow:hidden}
.hero-photo{left:0;top:0;width:1200px;height:548px;background:linear-gradient(90deg,#1a1a1a 0%,#6e6e6e 30%,#3a3a3a 48%,#0e0e0e 62%,#1c1c1c 100%)}
.hero-panel{left:700px;top:0;width:500px;height:548px;background:linear-gradient(160deg,#2a2a2a,#0a0a0a);clip-path:polygon(30% 0,100% 0,100% 100%,0 100%)}
.hero-products{left:680px;top:160px;width:440px;height:340px;border-radius:6px;background:linear-gradient(135deg,#f0b43a 0%,#c98a1d 35%,#151515 60%,#050505 100%)}
.site-logo{left:60px;top:58px;font-family:'Cinzel',serif;font-size:8.5px;color:var(--gold);letter-spacing:1.5px;font-weight:500;white-space:nowrap}
.nav{top:37px;font-size:9px;font-weight:600;letter-spacing:.4px;color:#e6e6e6;white-space:nowrap}
.cart{left:762px;top:36px;font-size:9px;font-weight:600;color:#e6e6e6;display:flex;gap:5px;align-items:center;white-space:nowrap}
.user{left:836px;top:28px;width:30px;height:30px;border:1px solid #bbb;border-radius:50%}
.search{left:887px;top:28px;width:188px;height:31px;background:#000;border:1px solid #333;border-radius:3px;font-size:9px;color:#ddd;display:flex;align-items:center;gap:8px;padding-left:10px;white-space:nowrap}
.flag{top:40px;width:12px;height:8px}
.hero-brand{left:60px;top:352px;font-family:'Cinzel',serif;font-weight:500;font-size:33px;letter-spacing:7px;color:var(--gold);white-space:nowrap}
.arrow{top:266px;color:#999;font-size:14px}
.dot{top:530px;width:8px;height:8px;border-radius:50%;background:#888}

/* tabs */
.tabs{left:241px;top:614px;width:716px;height:33px;border-bottom:1px solid #c2c2c0;font-size:11px;font-weight:600}
.tab{position:absolute;top:0;color:#555}
.tab-active{color:var(--gold)}

/* activity band */
.activity{left:241px;top:662px;width:716px;height:149px;background:var(--band);text-align:center}
.activity h2{position:absolute;top:74px;width:100%;font-size:20px;font-weight:500}
.activity p{position:absolute;top:112px;width:100%;font-size:14px}

.card{width:226px;background:var(--card);border:1px solid #c9c9c7}
.post{top:827px;height:298px}
.post-media{position:absolute;left:7px;top:28px;width:210px;height:218px;background:#f6f6f6;display:flex;align-items:center;justify-content:center;font-size:10px;color:#bdbdbd}
.post-by{position:absolute;left:7px;top:252px;font-size:9px}
.post-note{position:absolute;top:276px;width:100%;text-align:center;font-size:9px;color:#c4c4c4}

.rule{left:241px;width:716px;height:1px;background:#c2c2c0}
.eyebrow{left:241px;width:716px;text-align:center;font-size:11px;font-weight:700;letter-spacing:.3px}
.lead{left:241px;width:716px;text-align:center;font-size:16px;color:#555}

.product{height:209px;background:var(--tile);border:1px solid #cfcfcd}
.product-img{position:absolute;left:50px;top:10px;width:126px;height:140px;border-radius:6px}
.img-dark{background:linear-gradient(160deg,#e9a42a 0 25%,#1b1b1b 26% 100%)}
.img-box{background:linear-gradient(135deg,#1a1a1a 0 40%,#f1b23c 41% 60%,#121212 61%)}
.img-orange{left:80px;width:66px;background:linear-gradient(180deg,#f39c3c,#e07a20)}
.product-name{position:absolute;left:5px;top:164px;font-size:10px;font-weight:700;white-space:nowrap}
.price{position:absolute;left:5px;top:182px;background:#fff;font-size:9px;font-weight:700;padding:3px 6px}

.button{left:493px;width:214px;height:38px;background:var(--btn);color:#eee;font-size:10px;font-weight:600;display:flex;align-items:center;justify-content:center}

/* contact */
.contact{left:957px;top:575px;width:221px;height:343px;background:#fff;box-shadow:0 1px 6px rgba(0,0,0,.25)}
.contact-head{height:33px;background:var(--gold);display:flex;align-items:center;padding-left:12px;gap:10px;font-size:9px;font-weight:600;color:#fff}
.contact-toggle{position:absolute;right:0;top:0;width:31px;height:33px;background:var(--gold-dark);color:#fff;display:flex;align-items:center;justify-content:center;font-size:11px}
.contact h3{position:absolute;left:10px;top:48px;font-size:10px;font-weight:700}
.contact p{position:absolute;left:10px;top:70px;font-size:9px;font-weight:600}
.field{position:absolute;left:10px;width:201px;height:31px;border:1px solid #ddd;display:flex;align-items:center;gap:12px;padding-left:12px;font-size:9px;color:#888}
.textarea{align-items:flex-start;padding-top:8px;height:80px}
.send{position:absolute;left:10px;top:300px;width:201px;height:31px;background:#000;color:#fff;font-size:9px;font-weight:600;display:flex;align-items:center;justify-content:center}

/* footer */
.footer{left:0;top:1983px;width:1200px;height:472px;background:var(--black)}
.footer-logo{left:248px;top:2103px;font-family:'Cinzel',serif;font-size:9px;color:var(--gold);letter-spacing:1.5px;white-space:nowrap}
.footer-about{left:248px;top:2128px;width:222px;font-size:9.5px;line-height:17px;color:var(--footer-text)}
.col{font-size:10px;line-height:22.8px;color:var(--footer-text)}
.col b{font-weight:500;display:block;margin-left:-8px}
.friends{left:0;top:2277px;width:1200px;text-align:center;color:#fff;font-size:14px}
.social{top:2312px;display:flex;align-items:center;gap:7px;font-size:10px;color:#bbb}
.social i{width:22px;height:22px;border:1px solid #666;border-radius:50%}
.footer-rule{left:241px;top:2359px;width:716px;height:1px;background:#333}
.legal{top:2386px;font-size:9px;color:#aaa;white-space:nowrap}
</style>
</head>
<body>

<header>
  <div class="abs hero">
    <div class="abs hero-photo" role="img" aria-label="Black and white portrait of a man opening his white shirt collar"></div>
    <div class="abs hero-panel"></div>
    <div class="abs hero-products" role="img" aria-label="Black and gold skincare tube and box"></div>
    <div class="abs site-logo">VELMOR CREST</div>
    <nav>
      <span class="abs nav" style="left:180px">HOME</span>
      <span class="abs nav" style="left:233px">PRODUCTS</span>
      <span class="abs nav" style="left:320px">ABOUT US</span>
      <span class="abs nav" style="left:390px">TUTORIALS</span>
      <span class="abs nav" style="left:466px">BLOG</span>
    </nav>
    <div class="abs cart">
      <svg width="14" height="12" viewBox="0 0 14 12" fill="none" stroke="#ddd"><path d="M1 1h2l2 7h7l1-5H4"/><circle cx="6" cy="10.5" r="1"/><circle cx="11" cy="10.5" r="1"/></svg>CART (0)
    </div>
    <div class="abs user">
      <svg width="28" height="28" viewBox="0 0 28 28" fill="none" stroke="#ccc"><circle cx="14" cy="11" r="3"/><path d="M8 20c1-4 11-4 12 0"/></svg>
    </div>
    <div class="abs search">
      <svg width="10" height="10" viewBox="0 0 10 10" fill="none" stroke="#ddd"><circle cx="4" cy="4" r="3"/><path d="M6.5 6.5L9 9"/></svg>Search Velmor Crest
    </div>
    <span class="abs flag" style="left:1090px;background:#3b4f9a"></span>
    <span class="abs flag" style="left:1108px;background:#d8d8d8;border-left:4px solid #2a8a3a;border-right:4px solid #c22"></span>
    <span class="abs flag" style="left:1126px;background:#b33"></span>
    <div class="abs hero-brand">VELMOR CREST</div>
    <span class="abs arrow" style="left:18px">&#8249;</span>
    <span class="abs arrow" style="left:1174px">&#8250;</span>
    <span class="abs dot" style="left:584px;background:#eee"></span>
    <span class="abs dot" style="left:596px"></span>
    <span class="abs dot" style="left:608px"></span>
  </div>
</header>

<main>
  <div class="abs tabs">
    <span class="tab" style="left:19px">Products</span>
    <span class="tab tab-active" style="left:108px">Activity</span>
  </div>

  <section class="abs activity">
    <svg class="abs" style="left:335px;top:22px" width="46" height="28" viewBox="0 0 46 28" fill="none" stroke="var(--red)" stroke-width="2.5"><circle cx="3" cy="14" r="2.5" fill="var(--red)"/><path d="M5 14h9l4-10 5 20 4-14 3 4h10"/><circle cx="43" cy="14" r="2.5" fill="var(--red)"/></svg>
    <h2>Improve your Activity Stream</h2>
    <p>Post your looks using our products</p>
  </section>

  <article class="abs card post" style="left:248px"><div class="post-media">Pictoloop</div><span class="post-by">| by</span><span class="post-note">A post shared by () on</span></article>
  <article class="abs card post" style="left:488px"><div class="post-media">Pictoloop</div><span class="post-by">| by</span><span class="post-note">A post shared by () on</span></article>
  <article class="abs card post" style="left:728px"><div class="post-media">Pictoloop</div><span class="post-by">| by</span><span class="post-note">A post shared by () on</span></article>

  <div class="abs rule" style="top:1173px"></div>
  <div class="abs eyebrow" style="top:1192px">SHOP UPDATES</div>
  <div class="abs lead" style="top:1220px">Product Launches, Discounts, And Updates From Shops You Follow.</div>

  <article class="abs card product" style="left:248px;top:1258px"><div class="product-img img-dark" role="img" aria-label="Black serum bottle with gold cap"></div><span class="product-name">Eaque Aperiam Ratione Voluptas</span><span class="price">500.0</span></article>
  <article class="abs card product" style="left:488px;top:1258px"><div class="product-img img-box" role="img" aria-label="Black and gold tube with box"></div><span class="product-name">Exercitationem</span><span class="price">500.0</span></article>
  <article class="abs card product" style="left:728px;top:1258px"><div class="product-img img-orange" role="img" aria-label="Orange cleanser bottle"></div><span class="product-name">Ut</span><span class="price">500.0</span></article>
  <div class="abs button" style="top:1495px">See New Shop Updates</div>

  <div class="abs rule" style="top:1580px"></div>
  <div class="abs eyebrow" style="top:1596px">OUR COMMUNITY</div>
  <div class="abs lead" style="top:1623px">Share And Connect With Our Community</div>

  <article class="abs card product" style="left:248px;top:1661px"><div class="product-img img-dark" role="img" aria-label="Black serum bottle with gold cap"></div><span class="product-name">Eaque Aperiam Ratione Voluptas</span><span class="price">500.0</span></article>
  <article class="abs card product" style="left:488px;top:1661px"><div class="product-img img-box" role="img" aria-label="Black and gold tube with box"></div><span class="product-name">Exercitationem</span><span class="price">500.0</span></article>
  <article class="abs card product" style="left:728px;top:1661px"><div class="product-img img-orange" role="img" aria-label="Orange cleanser bottle"></div><span class="product-name">Ut</span><span class="price">500.0</span></article>
  <div class="abs button" style="top:1897px">View The Blog</div>

  <aside class="abs contact">
    <div class="contact-head">
      <svg width="12" height="10" viewBox="0 0 12 10" fill="none" stroke="#fff"><rect x=".5" y=".5" width="8" height="6"/><path d="M4 8h7V3"/></svg>Contact Us
    </div>
    <span class="contact-toggle">&#8963;</span>
    <h3>How Can We Help You?</h3>
    <p>Please, leave us your message.</p>
    <div class="field" style="top:100px"><svg width="10" height="10" viewBox="0 0 10 10" fill="none" stroke="#333"><circle cx="5" cy="3" r="2"/><path d="M1 9c1-4 7-4 8 0"/></svg>Enter your name</div>
    <div class="field" style="top:137px"><svg width="11" height="9" viewBox="0 0 11 9" fill="none" stroke="#333"><rect x=".5" y=".5" width="10" height="8"/><path d="M.5.5l5 4 5-4"/></svg>Enter your email</div>
    <div class="field" style="top:175px"><svg width="10" height="10" viewBox="0 0 10 10" fill="none" stroke="#333"><path d="M2 1l2 2-1 1c1 2 2 3 3 3l1-1 2 2-1 1C4 9 1 6 1 2z"/></svg>Enter your phone</div>
    <div class="field textarea" style="top:213px">How can we help you?</div>
    <div class="send">Send Message</div>
  </aside>
</main>

<footer>
  <div class="abs footer"></div>
  <div class="abs footer-logo">VELMOR CREST</div>
  <p class="abs footer-about">Lorem ipsum dolor sit amet, consectetur adipiscing elit. Suspendisse varius enim in eros elementum tristique. Duis cursus, mi quis viverra ornare, eros dolor interdum nulla, ut commodo diam libero vitae erat. Aenean faucibus nibh et justo cursus id rutrum lorem imperdiet. Nunc ut sem vitae risus tristique posuere.</p>
  <div class="abs col" style="left:494px;top:2053px"><b>Resources</b>Licenses<br>Blog<br>Discussions<br>Products<br>Collections<br>Help Center</div>
  <div class="abs col" style="left:734px;top:2053px"><b>Company</b>About<br>Brand<br>Terms<br>Cookie Policy<br>Privacy Policy<br>Careers</div>
  <div class="abs friends">let's be friends</div>
  <div class="abs social" style="left:468px"><i></i>Fanwall</div>
  <div class="abs social" style="left:562px"><i></i>Chirpline</div>
  <div class="abs social" style="left:660px"><i></i>Pictoloop</div>
  <div class="abs footer-rule"></div>
  <span class="abs legal" style="left:259px">Privacy Policy</span>
  <span class="abs legal" style="left:336px">Terms Of Use</span>
  <span class="abs legal" style="left:411px">Return Policy</span>
  <span class="abs legal" style="left:727px">© Copyright 2018 Velmor Crest. All Rights Reserved.</span>
</footer>

</body>
</html>
```